business card - for laser marking

I need design (curve) for my business card (make with laser) size 85mm x 55mm. How it look business card with laser marking see attached picture.

color:
Background: white
text and icons black

Please include: one side
1. dominik vrhovec - direktor
2. phone: +386(0)41 726 193
+386(0)592 817 06
3. info@zlatorez.example
4. faecebook.com/Zlatorez.Ex
5. KP-ATELJE, Dominik Vrhovec s.p.
Brezova ulica 17, 1000 Ljubljana, SI
6. logo

Please include: second side
1. logo
2. www.zlatorez.example
3. Lasersko graviranje
ovitki telefonov, ohišja telefonov / tablic, nakit, ure, alu vizitke, dog-tagi, kemični svinčniki, orodja, noži, vžigalniki

Industry/Entity Type

Business

Contact Information for Business Card

Please include: one side
+386(0)592 817 06
3. info@zlatorez.example
6. logo

1. logo
2. www.zlatorez.example
3. Lasersko graviranje

Colors
000000
ffffff

Requirements
Must have
• I need design (curve) for my business card (make with laser) size 85mm x 55mm. How it look business card with laser marking see attached picture.
• color:
• Background: white
• text and icons black
• Please include: one side
• 1. dominik vrhovec - direktor
• 2. phone: +386(0)41 726 193
• +386(0)592 817 06
• 3. info@zlatorez.example
• 4. faecebook.com/Zlatorez.Ex
• 5. KP-ATELJE, Dominik Vrhovec s.p.
• Brezova ulica 17, 1000 Ljubljana, SI
• 6. logo
• Please include: second side
• 1. logo
• 2. www.zlatorez.example
• 3. Lasersko graviranje
• ovitki telefonov, ohišja telefonov / tablic, nakit, ure, alu vizitke, dog-tagi, kemični svinčniki, orodja, noži, vžigalniki

```html
<!DOCTYPE html>
<html lang="sl">
<head>
<meta charset="utf-8">
<title>Zlatorez – vizitka</title>
<link href="https://fonts.googleapis.com/css2?family=Roboto:wght@400;700&display=swap" rel="stylesheet">
<style>
  :root{
    --stage:#b2b2b2;
    --card:#3d3d3d;
    --ink:#ffffff;
    --icon-ink:#3d3d3d;
    --brand-accent:#63a135;
  }
  html,body{margin:0;padding:0;overflow:hidden}
  body{width:1200px;height:791px;background:var(--stage);position:relative;font-family:'Roboto',Arial,sans-serif;color:var(--ink)}
  .card{position:absolute;top:150px;width:316px;height:490px}
  .card--mono{left:245px}
  .card--color{left:638px}
  .card-shape{position:absolute;inset:0;width:316px;height:490px}
  .card-shape path{fill:var(--card)}
  .brand{position:absolute;left:68px;width:200px;top:106px;display:flex;justify-content:center;align-items:center;gap:8px}
  .brand-dot{width:12px;height:12px;border-radius:50%;background:var(--ink)}
  .brand-name{font-weight:700;font-size:23px;letter-spacing:1.5px;color:var(--ink)}
  .card--color .brand-dot{background:var(--brand-accent)}
  .card--color .brand-name{color:var(--brand-accent)}
  .person{position:absolute;left:29px;top:235px}
  .person-name{font-weight:700;font-size:24px;line-height:1;margin:0}
  .person-role{font-size:14px;margin-top:5px}
  .contacts{position:absolute;left:29px;top:308px;list-style:none;margin:0;padding:0;font-size:14.4px}
  .contact{position:absolute;left:0;display:flex;align-items:flex-start;gap:10px;white-space:nowrap;line-height:21px}
  .contact-icon{width:19px;height:19px;border-radius:3px;background:var(--ink);flex:none;margin-top:1px;display:flex;align-items:center;justify-content:center}
  .contact-icon svg{width:13px;height:13px;fill:var(--icon-ink)}
  .c1{top:0}.c2{top:23px}.c3{top:55px}.c4{top:78px}.c5{top:108px}
</style>
</head>
<body>

<div class="card card--mono">
  <svg class="card-shape" viewBox="0 0 316 490" aria-hidden="true"><path d="M13.6 56 C40 20 80 0 110 2 C135 4 150 12 159 15 C175 8 200 0 227 0 C280 0 316 50 316 114 V474 Q316 490 300 490 H16 Q0 490 0 474 V180 A64 64 0 0 0 13.6 56 Z"/></svg>
  <div class="brand"><span class="brand-dot"></span><span class="brand-name">ZLATOREZ</span></div>
  <div class="person"><h1 class="person-name">Dominik Vrhovec</h1><div class="person-role">Direktor</div></div>
  <ul class="contacts">
    <li class="contact c1"><span class="contact-icon"><svg viewBox="0 0 16 16"><path d="M4 1h8a1 1 0 0 1 1 1v12a1 1 0 0 1-1 1H4a1 1 0 0 1-1-1V2a1 1 0 0 1 1-1zm1 2v8h6V3zm3 9a1 1 0 1 0 0 2 1 1 0 0 0 0-2z"/></svg></span>+386(0)41 726 193</li>
    <li class="contact c2"><span class="contact-icon"><svg viewBox="0 0 16 16"><path d="M3.5 1.5l2.5 3-1.5 1.6c.8 2 2.4 3.6 4.4 4.4L10.5 9l3 2.5-1.2 2.3C7 13.5 2.5 9 2.2 2.7z"/></svg></span>+386(0)592 817 06</li>
    <li class="contact c3"><span class="contact-icon"><svg viewBox="0 0 16 16"><path d="M1 3.5h14v9H1zm1.5 1.2v.3L8 9l5.5-4v-.3zM2.5 6.6v4.6h11V6.6L8 10.6z"/></svg></span>info@zlatorez.example</li>
    <li class="contact c4"><span class="contact-icon"></span>facebook.com/Zlatorez.Ex</li>
    <li class="contact c5"><span class="contact-icon"><svg viewBox="0 0 16 16"><path d="M8 1a5 5 0 0 0-5 5c0 3.5 5 9 5 9s5-5.5 5-9a5 5 0 0 0-5-5zm0 3a2 2 0 1 1 0 4 2 2 0 0 1 0-4z"/></svg></span>KP-ATELJE, Dominik Vrhovec s.p.<br>Brezova ulica 17, 1000 Ljubljana, SI</li>
  </ul>
</div>

<div class="card card--color">
  <svg class="card-shape" viewBox="0 0 316 490" aria-hidden="true"><path d="M13.6 56 C40 20 80 0 110 2 C135 4 150 12 159 15 C175 8 200 0 227 0 C280 0 316 50 316 114 V474 Q316 490 300 490 H16 Q0 490 0 474 V180 A64 64 0 0 0 13.6 56 Z"/></svg>
  <div class="brand"><span class="brand-dot"></span><span class="brand-name">ZLATOREZ</span></div>
  <div class="person"><h1 class="person-name">Dominik Vrhovec</h1><div class="person-role">Direktor</div></div>
  <ul class="contacts">
    <li class="contact c1"><span class="contact-icon"><svg viewBox="0 0 16 16"><path d="M4 1h8a1 1 0 0 1 1 1v12a1 1 0 0 1-1 1H4a1 1 0 0 1-1-1V2a1 1 0 0 1 1-1zm1 2v8h6V3zm3 9a1 1 0 1 0 0 2 1 1 0 0 0 0-2z"/></svg></span>+386(0)41 726 193</li>
    <li class="contact c2"><span class="contact-icon"><svg viewBox="0 0 16 16"><path d="M3.5 1.5l2.5 3-1.5 1.6c.8 2 2.4 3.6 4.4 4.4L10.5 9l3 2.5-1.2 2.3C7 13.5 2.5 9 2.2 2.7z"/></svg></span>+386(0)592 817 06</li>
    <li class="contact c3"><span class="contact-icon"><svg viewBox="0 0 16 16"><path d="M1 3.5h14v9H1zm1.5 1.2v.3L8 9l5.5-4v-.3zM2.5 6.6v4.6h11V6.6L8 10.6z"/></svg></span>info@zlatorez.example</li>
    <li class="contact c4"><span class="contact-icon"></span>facebook.com/Zlatorez.Ex</li>
    <li class="contact c5"><span class="contact-icon"><svg viewBox="0 0 16 16"><path d="M8 1a5 5 0 0 0-5 5c0 3.5 5 9 5 9s5-5.5 5-9a5 5 0 0 0-5-5zm0 3a2 2 0 1 1 0 4 2 2 0 0 1 0-4z"/></svg></span>KP-ATELJE, Dominik Vrhovec s.p.<br>Brezova ulica 17, 1000 Ljubljana, SI</li>
  </ul>
</div>

</body>
</html>
```